Plumbing & Heating bussiness card design

i do all plumbing and heating work and need a catchy design. keep it simple but eye catching nothing gimicky
i do 24hr call outs
landlord safety checks
all aspects of plumbing and heating
boiler breakdowns
flue sure reg number 804617
i have put up my old card. not to bothered about the front but i have put up the back for the details. mobile number and office are the same and the email has changed to tolwenpipes@mailvoro.net

Industry/Entity Type

Safety

Contact Information for Business Card

i do 24hr call outs
landlord safety checks
boiler breakdowns

Requirements
Must have
• i do 24hr call outs
• landlord safety checks
• all aspects of plumbing and heating
• boiler breakdowns
• flue sure reg number 804617

```html
<!DOCTYPE html>
<html lang="en">
<head>
<meta charset="utf-8">
<title>A Tolwen Plumbing &amp; Heating – Business Card</title>
<link rel="stylesheet" href="https://fonts.googleapis.com/css2?family=Open+Sans:wght@400;600;700;800&display=swap">
<style>
  :root {
    --backdrop: #2b2b2d;
    --brand-blue: #1a7fcf;
    --brand-blue-light: #23a3e3;
    --brand-blue-deep: #1470c0;
    --brand-red: #c8202f;
    --ink: #333a40;
    --paper: #ffffff;
    --badge-neutral: #d9dde1;
  }
  * { box-sizing: border-box; margin: 0; padding: 0; }
  html, body {
    width: 1200px; height: 900px; overflow: hidden;
    background: var(--backdrop);
    font-family: "Open Sans", Arial, sans-serif;
  }
  .stage { position: relative; width: 1200px; height: 900px; }

  .card {
    position: absolute;
    width: 600px; height: 340px;
    border-radius: 22px;
    overflow: hidden;
    box-shadow: 0 18px 40px rgba(0,0,0,0.45);
  }

  /* Front card */
  .card--front {
    left: 110px; top: 80px;
    background: linear-gradient(135deg, var(--brand-blue-deep) 0%, var(--brand-blue-light) 60%, var(--brand-blue) 100%);
    color: var(--paper);
  }
  .card--front .edge-stripe {
    position: absolute; top: 0; bottom: 0; right: 14px; width: 26px;
    background: var(--brand-red);
  }
  .card--front .brand {
    position: absolute; top: 54px; left: 230px; width: 310px;
    text-align: center;
  }
  .brand-name {
    display: flex; align-items: center; justify-content: center; gap: 10px;
    font-weight: 800; font-size: 30px; line-height: 1.05; letter-spacing: 0.5px;
    text-transform: uppercase;
  }
  .brand-name .brand-dot {
    width: 16px; height: 16px; border-radius: 50%; background: currentColor; flex: none;
  }
  .brand-sub {
    display: block; font-weight: 800; font-size: 19px; letter-spacing: 0.5px;
    text-transform: uppercase;
  }
  .card--front .services {
    position: absolute; left: 36px; bottom: 34px;
    list-style: none; font-size: 16px; line-height: 1.35; letter-spacing: 0.3px;
  }
  .services li { display: flex; align-items: center; gap: 10px; }
  .services li::before {
    content: ""; width: 9px; height: 9px; border-radius: 50%; background: var(--paper); flex: none;
  }

  /* Back card */
  .card--back {
    left: 490px; top: 480px;
    background: var(--paper);
    color: var(--ink);
  }
  .card--back .side-band {
    position: absolute; top: 0; bottom: 0; left: 22px; width: 26px;
    background: var(--brand-blue);
  }
  .card--back .brand {
    position: absolute; top: 40px; left: 78px;
    color: var(--ink);
  }
  .card--back .brand-name { justify-content: flex-start; font-size: 32px; }
  .card--back .brand-sub { text-align: left; font-size: 20px; }
  .card--back .rule {
    position: absolute; left: 170px; right: 0; top: 192px;
    height: 2px; background: var(--brand-red);
  }
  .badge {
    position: absolute; right: 30px; top: 30px;
    width: 58px; height: 58px; border-radius: 4px;
    background: var(--badge-neutral);
  }
  .contact { position: absolute; left: 78px; top: 176px; }
  .contact .person {
    font-weight: 800; font-size: 28px; color: var(--brand-blue);
    letter-spacing: 2px; text-transform: uppercase; line-height: 1;
    background: var(--paper); padding-right: 10px; display: inline-block;
    position: relative; z-index: 1;
  }
  .contact address {
    font-style: normal; font-size: 15px; line-height: 1.3; margin-top: 8px;
  }
  .contact .lines { list-style: none; margin-top: 6px; font-size: 15px; line-height: 1.35; }
  .contact .lines li { display: flex; align-items: center; gap: 10px; }
  .contact .lines svg { width: 13px; height: 13px; flex: none; }
</style>
</head>
<body>
<main class="stage">

  <section class="card card--front" aria-label="Business card front">
    <div class="edge-stripe"></div>
    <div class="brand">
      <span class="brand-name"><span class="brand-dot"></span>A Tolwen</span>
      <span class="brand-sub">Plumbing &amp; Heating</span>
    </div>
    <ul class="services">
      <li>I do 24hr call outs</li>
      <li>Landlord safety checks</li>
      <li>All aspects of plumbing and heating</li>
      <li>Boiler breakdowns</li>
      <li>Flue sure reg number 804617</li>
    </ul>
  </section>

  <section class="card card--back" aria-label="Business card back">
    <div class="side-band"></div>
    <div class="brand">
      <span class="brand-name"><span class="brand-dot"></span>A Tolwen</span>
      <span class="brand-sub">Plumbing &amp; Heating</span>
    </div>
    <div class="badge" role="img" aria-label="Registration badge"></div>
    <div class="rule"></div>
    <div class="contact">
      <span class="person">Rhys</span>
      <address>42 Harlowe Rd<br>Kestrelby, KB4 2QT</address>
      <ul class="lines">
        <li>
          <svg viewBox="0 0 14 14" aria-hidden="true"><rect x="3.5" y="1" width="7" height="12" rx="1.5" fill="none" stroke="var(--brand-blue)" stroke-width="1.5"/><circle cx="7" cy="10.8" r="0.9" fill="var(--brand-blue)"/></svg>
          07700 900318
        </li>
        <li>
          <svg viewBox="0 0 14 14" aria-hidden="true"><path d="M3 1.5l2.2 2.6-1.2 1.6c.8 1.8 2.2 3.2 4 4l1.6-1.2 2.6 2.2-1.4 1.8C6 12.3 1.7 8 1.2 2.9z" fill="var(--brand-blue)"/></svg>
          01632 960457
        </li>
        <li>
          <svg viewBox="0 0 14 14" aria-hidden="true"><rect x="1" y="3" width="12" height="8.5" rx="1" fill="none" stroke="var(--brand-blue)" stroke-width="1.4"/><path d="M1.5 3.6L7 8l5.5-4.4" fill="none" stroke="var(--brand-blue)" stroke-width="1.4"/></svg>
          tolwenpipes@mailvoro.net
        </li>
      </ul>
    </div>
  </section>

</main>
</body>
</html>
```